Web Concept Design - modernize website

Looking to modernize our current website. http :// hvkwmaplebrook . com

Color Scheme: Use uploaded palette. (Black, Silver, Dark Purple, Greyish Blue)

The website needs to have a patient-friendly, community-friendly feel to it. While still being a professional medical website. We don't want it to have a cold, clinical feel.

Information on home page needs to be split into their own separate pages with designs for each.

Home Page:
Lantern Walk-In & Family Care is a family practice and urgent care clinic dedicated to providing high quality, compassionate health care, to patients of all ages.
Hours of operation:
Monday-Friday 9am-6:30pm
Saturday: CLOSED
Sunday: CLOSED
Primary Care visits will be by appointment only.
We will accept our last new patient at 6:00p and our last established patient at 6:30p.
We will no longer be doing DOT Physicals.

At bottom of home page:

Lantern Walk-In & Family Care understands that information about your health is private and we know how important it is to keep your medical information protected. We follow all HIPAA guidelines to protect the privacy of your medical records. The privacy act below explains our privacy practices and how we may use and disclose your medical information. If you would like for Lantern Walk-In & Family Care to release any or all of your medical information to others, you can make the request by signing a release and bring it with you at your next visit. If you would like to contact someone about the privacy and/or use of your medical information, you may contact us at 205-318-7602.

Click here for HIPAA document.

Click here for Medical Release form.

---------------

Services Page:
We provide family and urgent care for patients of all ages.

-Annual physicals
-Pre-employment drug screening
-Women's care including pap smears
-Screening and treatment for diabetes, hypertension and cholesterol
-All minor trauma such as abscesses, lacerations, burns and fractures
-Minor skin complaints
-Onsite LAB/XRAY/EKG
-Weight loss
-Adult and Pediatric Vaccinations
-Osteopathic manual medicine
-Medical pain management

-----

Payment & Insurance Page:
We now have online bill pay for patient balances. Please visit https://secure.paynestclinic.com/lwfc382pay to pay your bill today!

We currently accept all forms of insurance with the exception of Medicaid. Please bring a copy of your insurance card and photo ID upon visit. We are also a Veltrix prime provider. We do accept self-pay for patients who do not have insurance.

----

Meet Our Providers Page:

Dr. Stephen (Steve) Hadley, DO
Family Practice Physician

Professional Experience
April 4, 2010 to Present Lantern Walk-In & Family Care Owner
12 years of Emergency Medicine experience
6/1994 - 7/1997 NMI Birmingham, AL
Family Medicine Residency
10/1997 to Present Board Certified in Family Medicine
Recertified 2004
Education
9/1990 to 5/1994 Fairhaven Institute of Osteopathic Studies
Old Westbury, New York
Degree: Doctor of Osteopathic Medicine
9/1985 to 5/1989 Carrow-Lindell College
Birmingham, Alabama
Degree: Bachelor of Science
Membership
National Guild of Household Clinicians
Physicians Council of the Gulf Territory

----

Navigation Bar should have links for all the above pages + NEW PATIENTS + Access Your Medical Records (feel free to be creative with how you design this). We don't want the navigation bar to be too crowded.

Target Market(s)

Medical Patients

Number of Pages Required

5+ page

Colors

Designer to choose colors to be used in the design.

Requirements
Must have
• Designs for all pages
• Keep it professional
Nice to have
• Be creative!
Should not have
• No cold clinical, medical websites

```html
<!DOCTYPE html>
<html lang="en">
<head>
<meta charset="utf-8">
<title>Lantern Walk-In &amp; Family Care</title>
<link rel="stylesheet" href="https://fonts.googleapis.com/css2?family=Fira+Sans:wght@500;600;700&family=Signika:wght@300;400;600&display=swap">
<style>
:root{
  --purple:#52207a;
  --ink:#2b2b2b;
  --white:#ffffff;
}
*{box-sizing:border-box;margin:0;padding:0}
html,body{width:1200px;height:3754px;overflow:hidden;background:var(--white)}
body{position:relative;font-family:"Signika",sans-serif;font-weight:300;color:var(--ink)}
.abs{position:absolute}
a{color:var(--purple);text-decoration:none}

/* header */
.topbar{left:0;top:0;width:1200px;height:119px;background:var(--purple)}
.brand{left:16px;top:36px;color:var(--white);font-family:"Fira Sans",sans-serif;font-weight:700;font-size:30px;line-height:36px;letter-spacing:.5px}
.contact-row{display:flex;align-items:center;gap:34px;color:var(--white);font-family:"Fira Sans",sans-serif;font-weight:600;font-size:12px;white-space:nowrap}
.contact-row .item{display:flex;align-items:center;gap:14px}
.contact-row svg{fill:var(--white)}
.social{display:flex;gap:12px;margin-left:30px}
.social span{width:26px;height:26px;border:2px solid var(--white);border-radius:50%}
.head-contact{left:16px;top:8px}
.mainnav{right:20px;top:62px;display:flex;gap:46px;font-family:"Fira Sans",sans-serif;font-weight:600;font-size:16px;color:var(--white);letter-spacing:.5px}
.mainnav a{color:inherit}
.subbar{left:0;top:119px;width:1200px;height:80px;background:var(--white);box-shadow:0 6px 10px rgba(0,0,0,.12)}
.hours{left:16px;top:8px;font-family:"Fira Sans",sans-serif;font-weight:700;font-size:20px;line-height:36px;color:var(--purple)}
.subnav{right:28px;top:26px;display:flex;gap:48px;font-family:"Fira Sans",sans-serif;font-weight:600;font-size:16px;color:var(--purple);letter-spacing:.3px}

/* section titles */
.section-title{left:0;width:1200px;text-align:center;font-family:"Fira Sans",sans-serif;font-weight:700;font-size:46px;line-height:56px;letter-spacing:3px;color:var(--ink)}
.body-text{font-size:23px;line-height:26.5px;letter-spacing:1.6px}
.body-text p+p{margin-top:26.5px}

.photo{position:absolute}
.ph-paper{background:linear-gradient(135deg,#e9ebee,#b7bec7)}
.ph-teal{background:linear-gradient(135deg,#aab9c3,#d7dde2)}
.ph-warm{background:linear-gradient(135deg,#d9c9b4,#8e98a2)}
.ph-dark{background:linear-gradient(135deg,#8a9099,#4d545c)}
.ph-blue{background:linear-gradient(160deg,#dfe6ee,#9bb3cc)}

/* services */
.service-grid{left:16px;top:1505px;display:grid;grid-template-columns:repeat(6,186px);grid-auto-rows:183px;gap:14px 10px}
.service{background:var(--purple);color:var(--white);display:flex;align-items:center;justify-content:center;text-align:center;padding:0 8px;font-size:23px;line-height:26px;font-weight:300;letter-spacing:.5px}

/* providers */
.provider-name{left:16px;top:2915px;font-family:"Fira Sans",sans-serif;font-weight:700;font-size:32px;line-height:37px;color:var(--purple)}
.provider-detail{left:16px;top:3021px;width:625px;font-size:22px;line-height:27.3px;letter-spacing:1.5px}

/* footer */
.footer{left:0;top:3576px;width:1200px;height:178px;background:var(--purple);color:var(--white)}
.footer-blurb{left:16px;top:14px;width:640px;font-size:17px;line-height:20px;font-weight:300;letter-spacing:.8px}
.footer-brand{right:18px;top:16px;text-align:right;font-family:"Fira Sans",sans-serif;font-weight:700;font-size:30px;line-height:36px}
.footer-contact{left:16px;top:100px}
.copyright{left:0;top:146px;width:1200px;text-align:center;font-size:16px;letter-spacing:.5px}
</style>
</head>
<body>

<header>
  <div class="abs topbar">
    <div class="abs contact-row head-contact">
      <div class="item"><svg width="20" height="20" viewBox="0 0 24 24"><path d="M6.6 10.8a15 15 0 0 0 6.6 6.6l2.2-2.2a1 1 0 0 1 1-.25 11.4 11.4 0 0 0 3.6.57 1 1 0 0 1 1 1V20a1 1 0 0 1-1 1A17 17 0 0 1 3 4a1 1 0 0 1 1-1h3.5a1 1 0 0 1 1 1c0 1.25.2 2.45.57 3.57a1 1 0 0 1-.25 1z"/></svg>205.318.7602</div>
      <div class="item"><svg width="22" height="20" viewBox="0 0 24 22"><rect x="6" y="0" width="12" height="6"/><rect x="1" y="7" width="22" height="9" rx="2"/><rect x="6" y="13" width="12" height="8"/></svg>205.447.1938</div>
      <div class="item"><svg width="28" height="20" viewBox="0 0 28 20"><rect x="0" y="0" width="28" height="20"/><path d="M1 1l13 10L27 1" stroke="#52207a" stroke-width="2" fill="none"/></svg>lanternwalkin@postfield.com</div>
      <div class="item" style="margin-left:10px"><svg width="18" height="24" viewBox="0 0 18 24"><path d="M9 0a9 9 0 0 0-9 9c0 7 9 15 9 15s9-8 9-15a9 9 0 0 0-9-9zm0 12.5A3.5 3.5 0 1 1 9 5.5a3.5 3.5 0 0 1 0 7z"/></svg>2281 Orchard Bend Road Suite 204&nbsp;&nbsp;Maplebrook, AL 35990</div>
      <div class="social"><span></span><span></span><span></span></div>
    </div>
    <div class="abs brand">LANTERN WALK-IN &amp;<br>FAMILY CARE</div>
    <nav class="abs mainnav"><a>HOME</a><a>SERVICES</a><a>PAYMENT &amp; INSURANCE</a><a>OUR PROVIDERS</a></nav>
  </div>
  <div class="abs subbar">
    <div class="abs hours">Monday - Friday: 9am - 6:30pm<br>Saturday, Sunday: CLOSED</div>
    <nav class="abs subnav"><a>NEW PATIENTS</a><a>ACCESS YOUR MEDICAL RECORDS</a></nav>
  </div>
</header>

<main>
  <section class="home">
    <h1 class="abs section-title" style="top:258px">LANTERN WALK-IN &amp; FAMILY CARE</h1>
    <div class="abs body-text" style="left:16px;top:350px;width:600px">
      <p>Lantern Walk-In &amp; Family Care is a family practice and urgent care clinic dedicated to providing high quality, compassionate health care, to patients of all ages.</p>
      <p>Primary Care visits will be by appointment only.</p>
      <p>We will accept our last new patient at 6:00p and our last established patient at 6:30p.</p>
    </div>
    <div class="photo ph-paper" style="left:627px;top:356px;width:553px;height:371px" role="img" aria-label="Doctor filling in a report form with a pen and stethoscope on the desk"></div>
    <div class="photo ph-teal" style="left:16px;top:727px;width:605px;height:361px" role="img" aria-label="Patient having blood pressure measured at a table"></div>
    <div class="photo ph-paper" style="left:16px;top:1104px;width:289px;height:178px" role="img" aria-label="Medical instruments laid out on a table"></div>
    <div class="photo ph-warm" style="left:324px;top:1104px;width:300px;height:178px" role="img" aria-label="Vaccination being given in an upper arm"></div>
    <div class="abs body-text" style="left:647px;top:745px;width:548px">
      <p>Lantern Walk-In &amp; Family Care understands that information about your health is private and we know how important it is to keep your medical information protected. We follow all HIPAA guidelines to protect the privacy of your medical records. The privacy act below explains our privacy practices and how we may use and disclose your medical information.</p>
      <p>If you would like for Lantern Walk-In &amp; Family Care to release any or all of your medical information to others, you can make the request by signing a release and bring it with you at your next visit. If you would like to contact someone about the privacy and/or use of your medical information, you may contact us at 205-318-7602.</p>
      <p><a>Click here</a> for HIPAA document.</p>
    </div>
  </section>

  <section class="services">
    <h2 class="abs section-title" style="top:1342px">SERVICE</h2>
    <p class="abs body-text" style="left:0;top:1430px;width:1200px;text-align:center">We provide family and urgent care for patients of all.</p>
    <div class="abs service-grid">
      <div class="service">Annual physicals</div>
      <div class="service">Pre-employment drug</div>
      <div class="service">Women's care including pap</div>
      <div class="service">Screening and treatment for diabetes, hypertension and cholesterol</div>
      <div class="service">All minor trauma such as abscesses, lacerations, burns and fractures</div>
      <div class="service">Minor skin complaints</div>
      <div class="service">Onsite LAB/XRAY/EKG</div>
      <div class="service">Weight loss</div>
      <div class="service">Adult and Pediatric Vaccinations</div>
      <div class="service">Osteopathic manual medicine</div>
      <div class="service">Medical pain management</div>
    </div>
  </section>

  <section class="payment">
    <h2 class="abs section-title" style="top:1945px">PAYMENT &amp; INSURANCE</h2>
    <div class="abs body-text" style="left:16px;top:2040px;width:785px">
      <p>We now have online bill pay for patient balances. Please visit https://secure.paynestclinic.com/lwfc382pay to pay your bill today!</p>
      <p>We currently accept all forms of insurance with the exception of Medicaid. Please bring a copy of your insurance card and photo ID upon visit. We are also a Veltrix prime provider. We do accept self-pay for patients who do not have insurance.</p>
    </div>
    <div class="photo ph-warm" style="left:812px;top:2042px;width:369px;height:247px" role="img" aria-label="Doctor's coat pocket with pens and a stethoscope"></div>
    <div class="photo ph-dark" style="left:812px;top:2310px;width:369px;height:457px" role="img" aria-label="Coffee cup and stethoscope on a desk"></div>
    <div class="photo ph-paper" style="left:16px;top:2265px;width:401px;height:223px" role="img" aria-label="Calculator and pen on paperwork"></div>
    <div class="photo ph-teal" style="left:16px;top:2512px;width:401px;height:255px" role="img" aria-label="Stethoscope beside a laptop and phone"></div>
    <div class="photo ph-paper" style="left:438px;top:2265px;width:353px;height:502px" role="img" aria-label="Hand filling in an insurance form on a clipboard"></div>
  </section>

  <section class="providers">
    <h2 class="abs section-title" style="top:2829px">MEET OUR PROVIDERS</h2>
    <h3 class="abs provider-name">Dr. Stephen (Steve) Hadley, DO<br>Family Practice Physician</h3>
    <div class="abs provider-detail">
      Professional Experience<br>
      April 4, 2010 to Present&nbsp;&nbsp;&nbsp;Lantern Walk-In &amp; Family Care Owner<br>
      12 years of Emergency Medicine experience<br>
      6/1994 - 7/1997&nbsp;&nbsp;&nbsp;&nbsp;NMI Birmingham, AL<br>
      Family Medicine Residency<br>
      10/1997 to Present&nbsp;&nbsp;&nbsp;Board Certified in Family Medicine<br>
      Recertified 2004<br>
      Education<br>
      9/1990 to 5/1994 Fairhaven Institute of Osteopathic Studies<br>
      Old Westbury, New York<br>
      Degree: Doctor of Osteopathic Medicine<br>
      9/1985 to 5/1989&nbsp;&nbsp;Carrow-Lindell College<br>
      Birmingham, Alabama<br>
      Degree: Bachelor of Science<br>
      Membership<br>
      National Guild of Household Clinicians
    </div>
    <div class="photo ph-blue" style="left:714px;top:2921px;width:467px;height:589px" role="img" aria-label="Portrait of the physician in blue scrubs and surgical cap"></div>
  </section>
</main>

<footer class="abs footer">
  <p class="abs footer-blurb">Lantern Walk-In &amp; Family Care is a family practice and urgent care clinic dedicated to providing high quality, compassionate health care, to patients of all ages.</p>
  <div class="abs footer-brand">LANTERN WALK-IN<br>&amp; FAMILY CARE</div>
  <div class="abs contact-row footer-contact">
    <div class="item"><svg width="20" height="20" viewBox="0 0 24 24"><path d="M6.6 10.8a15 15 0 0 0 6.6 6.6l2.2-2.2a1 1 0 0 1 1-.25 11.4 11.4 0 0 0 3.6.57 1 1 0 0 1 1 1V20a1 1 0 0 1-1 1A17 17 0 0 1 3 4a1 1 0 0 1 1-1h3.5a1 1 0 0 1 1 1c0 1.25.2 2.45.57 3.57a1 1 0 0 1-.25 1z"/></svg>205.318.7602</div>
    <div class="item"><svg width="22" height="20" viewBox="0 0 24 22"><rect x="6" y="0" width="12" height="6"/><rect x="1" y="7" width="22" height="9" rx="2"/><rect x="6" y="13" width="12" height="8"/></svg>205.447.1938</div>
    <div class="item"><svg width="28" height="20" viewBox="0 0 28 20"><rect x="0" y="0" width="28" height="20"/><path d="M1 1l13 10L27 1" stroke="#52207a" stroke-width="2" fill="none"/></svg>lanternwalkin@postfield.com</div>
    <div class="item" style="margin-left:10px"><svg width="18" height="24" viewBox="0 0 18 24"><path d="M9 0a9 9 0 0 0-9 9c0 7 9 15 9 15s9-8 9-15a9 9 0 0 0-9-9zm0 12.5A3.5 3.5 0 1 1 9 5.5a3.5 3.5 0 0 1 0 7z"/></svg>2281 Orchard Bend Road Suite 204&nbsp;&nbsp;Maplebrook, AL 35990</div>
    <div class="social"><span></span><span></span><span></span></div>
  </div>
  <p class="abs copyright">All rights reserved © 2018. Lantern Walk-In &amp; Family Care</p>
</footer>

</body>
</html>
```